Employee Benefits and Insurance Consulting

We are an existing company with over 30 years experience but are changing our name. We would like a simple design with grey tones.

Industry/Entity Type

Insurance

Contact Information for Business Card

Marlow Benefits Consulting
Gerald P Odell CEO
5172 Brackenfield Road
Louisville, TN 37777
gerald@marlowbx.com
865-412-3396 - O
865-247-5081 - C

```html
<!DOCTYPE html>
<html lang="en">
<head>
<meta charset="utf-8">
<title>Marlow Benefits Consulting – Business Card</title>
<link rel="stylesheet" href="https://fonts.googleapis.com/css2?family=Open+Sans:wght@400;700&display=swap">
<style>
  :root {
    --page: #ffffff;
    --card: #666666;
    --card-edge: #5a5a5a;
    --ink: #b4b4b4;
    --ink-soft: #b8b8b8;
  }
  html, body {
    margin: 0;
    padding: 0;
    width: 1200px;
    height: 704px;
    overflow: hidden;
    background: var(--page);
  }
  .business-card {
    position: relative;
    box-sizing: border-box;
    width: 1200px;
    height: 704px;
    background: var(--card);
    border: 2px solid var(--card-edge);
    border-radius: 24px;
    font-family: "Open Sans", "Segoe UI", sans-serif;
    color: var(--ink);
  }
  .brand-mark {
    position: absolute;
    left: 66px;
    top: 152px;
    width: 120px;
    height: 120px;
    background: var(--ink);
  }
  .company-name {
    position: absolute;
    left: 212px;
    top: 208px;
    margin: 0;
    font-size: 40px;
    font-weight: 700;
    line-height: 1.2;
    white-space: nowrap;
  }
  .divider {
    position: absolute;
    left: 66px;
    top: 327px;
    width: 1070px;
    height: 8px;
    background: var(--ink);
  }
  .person {
    position: absolute;
    left: 66px;
    top: 360px;
    margin: 0;
    font-size: 40px;
    font-weight: 700;
    line-height: 1.2;
    white-space: nowrap;
  }
  .person .role {
    font-size: 30px;
    font-weight: 400;
    color: var(--ink-soft);
  }
  .contact-list {
    position: absolute;
    left: 66px;
    top: 412px;
    margin: 0;
    padding: 0;
    list-style: none;
    font-size: 27px;
    line-height: 35px;
    color: var(--ink-soft);
    white-space: nowrap;
  }
  .contact-list li:last-child { margin-top: -3px; }
</style>
</head>
<body>
  <main class="business-card">
    <div class="brand-mark" aria-hidden="true"></div>
    <h1 class="company-name">Marlow Benefits Consulting</h1>
    <div class="divider" aria-hidden="true"></div>
    <p class="person">Gerald P Odell <span class="role">CEO</span></p>
    <ul class="contact-list">
      <li>O:- 865-412-3396</li>
      <li>E:- gerald@marlowbx.com</li>
      <li>C:- 865-247-5081</li>
      <li>A:- 5172 Brackenfield Road, Louisville, TN 37777</li>
    </ul>
  </main>
</body>
</html>
```